Tidewalk Intro Course QM Dive Bonaire

QM Dive is looking for a great flyer to promote our Tidewalk Intro Course around Bonaire, the Caribbean.

Bonaire is shore dive capital of the world.
Our guests rent a pick-up truck. we would like to inform them about the possibilities of the Tidewalk Intro Dive.

We have the logo, images and text available. Its the catchy and mind blowing design we are looking for to create an eye-catch flyer.
One side will be in English, the other side will be in Dutch.

Target Market(s)

Visitors (non divers) of the island Bonaire

Industry/Entity Type

Diving industry

Font styles to use
Sans Serif

Colors
0094D4
00A9DD
6FCCEA
C7EBF8
E9F6FB
F0912C
F2A743
F7CA91
FBE8D2
FDF5EE

Requirements
Must have
• The picture with the car and divers next to it is mandatory. Inspire to go for a tidewalk intro dive, show the beauty under water, easy to come dive with us, just takes half a day
Should not have
• Should not have pictures taken not around Bonaire.

```html
<!DOCTYPE html>
<html lang="en">
<head>
<meta charset="utf-8">
<title>Tidewalk Intro Dive – QM Dive Bonaire flyers</title>
<link href="https://fonts.googleapis.com/css2?family=Barlow+Condensed:ital,wght@0,600;1,600;1,700&family=Barlow:ital,wght@0,400;0,500;1,400&display=swap" rel="stylesheet">
<style>
  :root{
    --teal:#00776b;
    --blue:#0094D4;
    --blue-2:#00A9DD;
    --blue-3:#6FCCEA;
    --blue-4:#C7EBF8;
    --blue-5:#E9F6FB;
    --orange:#F0912C;
    --orange-2:#F2A743;
    --orange-4:#FBE8D2;
    --ink:#1d1d1d;
    --white:#ffffff;
  }
  *{box-sizing:border-box;margin:0;padding:0}
  html,body{width:1200px;height:1200px;overflow:hidden}
  body{background:var(--teal);position:relative;font-family:"Barlow",Arial,sans-serif;color:var(--ink)}
  .flyer{position:absolute;top:253px;width:494px;height:695px;background:var(--white);overflow:hidden;box-shadow:0 14px 28px rgba(0,0,0,.35)}
  .flyer--nl{left:76px}
  .flyer--en{left:623px}

  .hero-photo{position:absolute;left:0;top:0;width:494px;height:165px;
    background:linear-gradient(180deg,#2c8fd6 0%,#3f7fc4 45%,#7d6b74 75%,#9a7a4e 100%)}
  .body-tint{position:absolute;left:0;top:150px;width:494px;height:540px;background:var(--blue-5)}
  .body-white{position:absolute;left:0;top:440px;width:494px;height:160px;background:var(--white)}
  .waves{position:absolute;left:0;top:110px;width:494px;height:80px}

  .brand-box{position:absolute;left:180px;top:0;width:134px;height:63px;background:var(--white);
    display:flex;align-items:center;justify-content:center;gap:10px}
  .brand-name{font-family:"Barlow Condensed",Arial,sans-serif;font-weight:600;font-size:19px;color:var(--blue);letter-spacing:.5px}
  .partner-badge{width:26px;height:26px;border-radius:50%;background:var(--blue)}

  .title{position:absolute;left:102px;width:289px;text-align:center;font-family:"Barlow Condensed",Arial,sans-serif;font-style:italic;font-weight:700;color:var(--white);line-height:1}
  .title--top{top:137px;height:37px;background:var(--orange);font-size:34px;padding-top:2px}
  .title--bottom{top:174px;height:41px;background:var(--blue);font-size:36px;padding-top:3px}

  .intro{position:absolute;left:14px;top:221px;width:466px;text-align:center;font-style:italic;font-size:9.6px;line-height:1.45}

  .gallery{position:absolute;left:40px;top:256px;width:405px;height:205px}
  .tile{position:absolute}
  .tile--angelfish{left:0;top:0;width:147px;height:97px;background:linear-gradient(135deg,#1a2d3e,#4f7fa0 60%,#c9b94a)}
  .tile--school{left:150px;top:0;width:138px;height:97px;background:linear-gradient(160deg,#2a5a93,#7f9fbf 55%,#3d6f8f)}
  .tile--seahorse{left:291px;top:0;width:114px;height:205px;background:linear-gradient(180deg,#1a1410,#c26e1a 45%,#6a4a48 80%,#2b211c)}
  .tile--trunkfish{left:0;top:100px;width:147px;height:105px;background:linear-gradient(160deg,#2e6a86,#5a8a86 55%,#7a5a40)}
  .tile--coral{left:150px;top:100px;width:138px;height:105px;background:linear-gradient(170deg,#1f6fa8,#4f88a6 40%,#c9a56a 70%,#6a5a34)}

  .section-title{position:absolute;font-family:"Barlow Condensed",Arial,sans-serif;font-style:italic;font-weight:700;font-size:17px;line-height:.95;color:var(--blue)}
  .section-title span{display:block;color:var(--orange)}
  .facts{position:absolute;list-style:none}
  .facts li{font-size:6px;line-height:1.25;border-left:2px solid var(--blue-3);padding:0 0 1px 5px;margin-bottom:3px;position:relative}
  .facts li::after{content:"";position:absolute;left:7px;right:0;bottom:-2px;border-bottom:1px dashed var(--blue-4)}
  .facts li:last-child::after{display:none}
  .divider{position:absolute;left:223px;top:470px;width:2px;height:124px;background:var(--blue-4)}
  .paragraph{position:absolute;font-size:6px;line-height:1.3}

  .callout{position:absolute;left:338px;width:140px;border:1.5px dashed var(--blue-2);border-radius:8px;background:var(--orange-4);
    text-align:center;font-family:"Barlow Condensed",Arial,sans-serif;font-style:italic;font-weight:700;color:var(--blue);font-size:10.4px;line-height:1.2;padding:8px 4px}
  .callout .tag{display:inline-block;background:var(--orange);color:var(--white);padding:1px 4px;font-size:11.5px;margin-top:2px}

  .footer-photo{position:absolute;left:0;top:600px;width:494px;height:95px;
    background:linear-gradient(90deg,var(--blue) 0%,var(--blue-2) 28%,#b9dbe9 45%,#e6e0d2 70%,#8a8378 100%)}
  .footer-band{position:absolute;left:0;top:600px;width:494px;height:95px;
    background:linear-gradient(90deg,rgba(0,148,212,1) 0%,rgba(0,148,212,.9) 30%,rgba(0,148,212,0) 50%)}
  .contact{position:absolute;left:25px;top:626px;font-family:"Barlow Condensed",Arial,sans-serif;font-weight:600;color:var(--white);line-height:1}
  .contact .phone{font-size:15.5px}
  .contact .web{font-size:15px;margin-top:5px}
  .contact .mail{font-size:9.5px;margin-top:8px}
</style>
</head>
<body>

<article class="flyer flyer--nl" lang="nl">
  <div class="hero-photo" role="img" aria-label="Underwater reef scene with a sea turtle, sea fans and a school of blue fish"></div>
  <div class="body-tint"></div>
  <div class="body-white"></div>
  <svg class="waves" viewBox="0 0 494 80" preserveAspectRatio="none" aria-hidden="true">
    <path d="M0 20 C80 0 150 60 260 45 S420 10 494 30 V80 H0Z" fill="#C7EBF8"/>
    <path d="M0 40 C90 25 160 70 270 60 S420 35 494 45 V80 H0Z" fill="#6FCCEA"/>
    <path d="M0 58 C100 45 170 80 280 72 S430 55 494 62 V80 H0Z" fill="#0094D4"/>
    <path d="M0 68 C100 60 180 82 290 78 S430 68 494 72 V80 H0Z" fill="#E9F6FB"/>
  </svg>
  <div class="brand-box"><span class="brand-name">QM Dive</span><span class="partner-badge"></span></div>
  <h1 class="title title--top">Tidewalk Intro</h1>
  <h2 class="title title--bottom">Proefduik op Bonaire</h2>
  <p class="intro">Word verliefd op het gevoel van duiken in een onderwaterparadijs. Onder begeleiding van een duikinstructeur ontdek je op een makkelijke en leuke manier alle basisvaardigheden voor een heerlijke duik.</p>
  <div class="gallery">
    <div class="tile tile--angelfish" role="img" aria-label="French angelfish close-up"></div>
    <div class="tile tile--school" role="img" aria-label="School of grunts over the reef"></div>
    <div class="tile tile--seahorse" role="img" aria-label="Orange seahorse on coral"></div>
    <div class="tile tile--trunkfish" role="img" aria-label="Trunkfish beside a sea fan"></div>
    <div class="tile tile--coral" role="img" aria-label="Christmas tree worm on brain coral"></div>
  </div>

  <h3 class="section-title" style="left:19px;top:470px">Liefde voor het<span>waterleven</span></h3>
  <ul class="facts" style="left:19px;top:503px;width:98px">
    <li>Onze proefduik is voor iedereen vanaf 10 jaar.</li>
    <li>Na een korte theoretische introductie geniet je meteen van een duik.</li>
    <li>De activiteit duurt 3 tot 4 uur.</li>
    <li>Je kunt meedoen wanneer je gezond genoeg bent om jouw duikset te dragen.</li>
  </ul>
  <ul class="facts" style="left:121px;top:503px;width:96px">
    <li>Een groep bestaat uit maximaal 4 personen.</li>
    <li>Hierdoor ervaar je de pracht van de oceaan zonder afleiding van anderen.</li>
    <li>En heeft de duikinstructeur veel tijd voor persoonlijke aandacht.</li>
  </ul>
  <div class="divider"></div>
  <h3 class="section-title" style="left:233px;top:470px">Underwater<span>paradijs</span></h3>
  <p class="paragraph" style="left:233px;top:505px;width:97px">Bonaire is bij uitstek de plek voor een proefduik. Na een korte introductie stappen we direct de zee in waar het rif al vrij snel begint. Bovendien kennen we de perfecte duikspots voor beginners. Hier loopt de zeebodem in een langzaam tempo naar beneden en word je verrast door de mooiste vissen en koralen.</p>
  <div class="callout" style="top:486px">Kom gerust langs bij onze front&#8209;office. Wij zijn graag bereid je vragen te beantwoorden of om de<br><span class="tag">'Tidewalk Intro Dive'!</span><br>in te plannen.</div>

  <div class="footer-photo" role="img" aria-label="Two divers beside a white pick-up truck on a Bonaire beach with dive gear on the rocks"></div>
  <div class="footer-band"></div>
  <div class="contact">
    <p class="phone">Phone : +(599) 555 01 23</p>
    <p class="web">www.qmdive-bonaire.com</p>
    <p class="mail">E-mail : info@qmdive-bonaire.com</p>
  </div>
</article>

<article class="flyer flyer--en" lang="en">
  <div class="hero-photo" role="img" aria-label="Underwater reef scene with a sea turtle, sea fans and a school of blue fish"></div>
  <div class="body-tint"></div>
  <div class="body-white"></div>
  <svg class="waves" viewBox="0 0 494 80" preserveAspectRatio="none" aria-hidden="true">
    <path d="M0 20 C80 0 150 60 260 45 S420 10 494 30 V80 H0Z" fill="#C7EBF8"/>
    <path d="M0 40 C90 25 160 70 270 60 S420 35 494 45 V80 H0Z" fill="#6FCCEA"/>
    <path d="M0 58 C100 45 170 80 280 72 S430 55 494 62 V80 H0Z" fill="#0094D4"/>
    <path d="M0 68 C100 60 180 82 290 78 S430 68 494 72 V80 H0Z" fill="#E9F6FB"/>
  </svg>
  <div class="brand-box"><span class="brand-name">QM Dive</span><span class="partner-badge"></span></div>
  <h1 class="title title--top">Tidewalk Intro</h1>
  <h2 class="title title--bottom">Diving on Bonaire</h2>
  <p class="intro" style="font-size:10px">Fall in love with diving in our underwater paradise. Under the guidance of a dive instructor you will learn the basic skills for peaceful diving in a fun and easy way.</p>
  <div class="gallery">
    <div class="tile tile--angelfish" role="img" aria-label="French angelfish close-up"></div>
    <div class="tile tile--school" role="img" aria-label="School of grunts over the reef"></div>
    <div class="tile tile--seahorse" role="img" aria-label="Orange seahorse on coral"></div>
    <div class="tile tile--trunkfish" role="img" aria-label="Trunkfish beside a sea fan"></div>
    <div class="tile tile--coral" role="img" aria-label="Christmas tree worm on brain coral"></div>
  </div>

  <h3 class="section-title" style="left:19px;top:470px">Develop a passion<span>for marine life</span></h3>
  <ul class="facts" style="left:19px;top:503px;width:98px">
    <li>Ages 10 and up can sign up for our discover dive</li>
    <li>You'll dive straight into the water after a brief theoretic introduction</li>
    <li>The Tidewalk Intro Course will take 3-4 hours</li>
    <li>Before participating, you are required to fill out a medical questionnaire</li>
  </ul>
  <ul class="facts" style="left:121px;top:503px;width:96px">
    <li>A group consists of a maximum of 4 people</li>
    <li>Experience the splendor of the ocean without much distraction by other divers</li>
    <li>And enjoy a lot of personal attention given by your instructor</li>
  </ul>
  <div class="divider"></div>
  <h3 class="section-title" style="left:233px;top:470px">Underwater<span>paradise</span></h3>
  <p class="paragraph" style="left:233px;top:505px;width:86px">Bonaire is the place to learn how to scuba dive. After a brief introduction we will directly dive into the sea, where the reef starts in shallow waters. We know the perfect dive sites for beginners. Here, the sea bed slopes gradually down and you'll be amazed by the most beautiful fish and corals.</p>
  <div class="callout" style="top:491px;left:332px;width:142px;font-size:11.5px">Stop by at our Front office and we are happy to answer all your questions or to book your<br><span class="tag">'Tidewalk Intro Dive'!</span></div>

  <div class="footer-photo" role="img" aria-label="Two divers beside a white pick-up truck on a Bonaire beach with dive gear on the rocks"></div>
  <div class="footer-band"></div>
  <div class="contact">
    <p class="phone">Phone : +(599) 555 01 23</p>
    <p class="web">www.qmdive-bonaire.com</p>
    <p class="mail">E-mail : info@qmdive-bonaire.com</p>
  </div>
</article>

</body>
</html>
```